We currently have a good logo and we want business cards that can display our logo but also represent our industry - telecom construction - We are a construction company specializing in telecom construction such as installation of fiber optic cable throughout cities and across the country. Nationwide services
We are large enough to handle most any project yet small enough to be a flexible partner and resource.

Target Market(s)

U.S. based telecom carriers and providers

Industry/Entity Type

Construction

Contact Information for Business Card

Business cards should include our logo, phone number and website address. Also, including some information as to our core services would be good.

Colors

Designer to choose colors to be used in the design.

Requirements
Must have
• Colors based on logo
• Must use our logo
• Logo, name, email, website address, phone number
• Tovasco Conduit
• Brent Halvik
• Director of Business Development
• (555) 271-0386
• www.TVSQ-example.com
Nice to have
• Construction services including:
• Small Cell Construction
• Boring/Drilling
• Plowing / Trenching
• Conduit installation
• Fiber pulling
• splicing
• building entries
• Aerial construction
• Aerial Make Ready
• Make Ready Engineering
Should not have
• We are open to ideas

```html
<!DOCTYPE html>
<html lang="en">
<head>
<meta charset="utf-8">
<title>Tovasco Conduit — Business Card</title>
<link rel="stylesheet" href="https://fonts.googleapis.com/css2?family=Poppins:wght@800&family=Open+Sans:wght@300;400&display=swap">
<style>
  :root {
    --sky: #00bcf0;
    --ocean: #0090d4;
    --navy: #0064b0;
    --brand: #0a5cb0;
    --shadow: #a3a3a3;
    --paper: #ffffff;
    --ink: #111111;
    --text: #2a2a2a;
  }
  html, body {
    margin: 0;
    padding: 0;
    width: 1200px;
    height: 1000px;
    overflow: hidden;
    background: var(--paper);
  }
  .stage { display: block; width: 1200px; height: 1000px; }
  .card-paper { fill: var(--paper); }
  .card-shadow { fill: var(--shadow); }
  .band-sky { fill: var(--sky); }
  .band-ocean { fill: var(--ocean); }
  .band-navy { fill: var(--navy); }
  .wordmark {
    font-family: "Poppins", sans-serif;
    font-weight: 800;
    fill: var(--brand);
  }
  .holder-name {
    font-family: "Poppins", sans-serif;
    font-weight: 800;
    font-size: 48px;
    fill: var(--ink);
  }
  .holder-title, .contact-line {
    font-family: "Open Sans", sans-serif;
    font-weight: 300;
    font-size: 21px;
    fill: var(--text);
  }
  .contact-line { font-size: 22px; }
  .contact-icon { fill: none; stroke: var(--navy); stroke-width: 3; }
  .contact-icon-solid { fill: var(--navy); }
</style>
</head>
<body>
<svg class="stage" viewBox="0 0 2100 1750" xmlns="http://www.w3.org/2000/svg">

  <!-- Front card -->
  <g class="card-front">
    <rect class="card-shadow" x="1509" y="188" width="19" height="558"/>
    <rect class="card-shadow" x="596" y="722" width="932" height="24"/>
    <rect class="card-paper" x="577" y="188" width="932" height="534"/>
    <path class="band-sky" d="M577,600 Q1043,540 1509,360 L1509,400 Q1043,575 577,625 Z"/>
    <path class="band-ocean" d="M577,645 Q1043,595 1509,430 L1509,722 L577,722 Z"/>
    <path class="band-navy" d="M577,700 Q1043,670 1509,560 L1509,722 L577,722 Z"/>
    <text class="wordmark" x="735" y="350" font-size="62">Tovasco</text>
    <text class="wordmark" x="735" y="425" font-size="62">Conduit</text>
  </g>

  <!-- Back card -->
  <g class="card-back">
    <rect class="card-shadow" x="1528" y="958" width="22" height="559"/>
    <rect class="card-shadow" x="619" y="1488" width="931" height="29"/>
    <rect class="card-paper" x="619" y="927" width="909" height="561"/>
    <path class="band-navy" d="M1528,1120 Q1280,1260 1200,1488 L1225,1488 Q1300,1275 1528,1145 Z"/>
    <path class="band-ocean" d="M1528,1165 Q1310,1290 1245,1488 L1290,1488 Q1345,1310 1528,1210 Z"/>
    <path class="band-sky" d="M1528,1240 Q1370,1330 1320,1488 L1528,1488 Z"/>

    <text class="wordmark" x="1318" y="1028" font-size="26">Tovasco</text>
    <text class="wordmark" x="1318" y="1060" font-size="26">Conduit</text>

    <text class="holder-name" x="661" y="1036">Brent Halvik</text>
    <text class="holder-title" x="661" y="1080">Director of Business Development</text>

    <g class="contact-phone">
      <rect class="contact-icon" x="680" y="1245" width="18" height="29" rx="3"/>
      <circle class="contact-icon-solid" cx="689" cy="1270" r="1.8"/>
      <text class="contact-line" x="757" y="1268">(555) 271-0386</text>
    </g>
    <g class="contact-web">
      <g transform="rotate(-45 689 1341)">
        <rect class="contact-icon" x="672" y="1335" width="20" height="12" rx="3"/>
        <rect class="contact-icon" x="686" y="1335" width="20" height="12" rx="3"/>
      </g>
      <text class="contact-line" x="757" y="1345">www.TVSQ-example.com</text>
    </g>
  </g>
</svg>
</body>
</html>
```